website refresh with jungle and/or gorilla theme for marketing agency

Our marketing agency needs a creative website boost. The website (which is Wordpress) is:https://www.tallreedmedia.com. Given our name, we would like to have a jungle/gorilla theme. The Tallreed website should have a beastly presence. See the site now and how the gorilla is in your face. The text can remain the same, we just need a new layout and/or graphics. What other direction can I give? Not sure, we will know it when we see it.

Target Market(s)

small and medium sized businesses

Industry/Entity Type

Digital Marketing

Number of Pages Required

1 page

Colors

Designer to choose colors to be used in the design.

Requirements
Must have
• I don't really have any must have's. I don't want to limit the creativity of the designer.
Nice to have
• I am encouraging an out of the box design, something that isn't so "boxy" and traditional like the other sites.
Should not have
• I don't like standard looking sites that have a boxy layout with your standard cartoon and/or basic icons.

```html
<!DOCTYPE html>
<html lang="en">
<head>
<meta charset="utf-8">
<title>Tallreed Marketing</title>
<link rel="stylesheet" href="https://fonts.googleapis.com/css2?family=Montserrat:wght@400;600;700;800&family=Open+Sans:wght@400;600&display=swap">
<style>
:root{
  --teal:#25b5ac;
  --teal-dark:#1c948d;
  --ink:#141414;
  --night:#1b1c1d;
  --charcoal:#242627;
  --paper:#ebebeb;
  --white:#ffffff;
  --muted:#a9adb0;
  --text-dark:#2b2b2b;
}
*{box-sizing:border-box;margin:0;padding:0}
html,body{width:1200px;height:3380px;overflow:hidden;background:var(--ink)}
body{font-family:"Open Sans",Arial,sans-serif;color:var(--white);position:relative}
section,footer{position:absolute;left:0;width:1200px;overflow:hidden}

/* hero */
.hero{top:0;height:860px;background:#101112}
.hero-photo{position:absolute;left:380px;top:0;width:820px;height:860px;
  background:radial-gradient(ellipse at 62% 42%,#4a4d50 0%,#2a2c2e 35%,#141516 70%,#101112 100%)}
.logo{position:absolute;font-family:"Montserrat",Arial,sans-serif;font-weight:800;letter-spacing:1px;line-height:1}
.hero .logo{left:80px;top:56px;font-size:26px}
.logo small{display:block;font-size:12px;letter-spacing:3px;margin-top:6px;font-weight:700}
.logo .brand-name{color:var(--teal)}
.nav{position:absolute;right:80px;top:66px;display:flex;gap:34px;font-family:"Montserrat",Arial,sans-serif;font-size:12px;font-weight:700;letter-spacing:1px}
.hero-copy{position:absolute;left:80px;top:250px;width:760px}
.hero-title{font-family:"Montserrat",Arial,sans-serif;font-weight:800;font-size:50px;line-height:1.12;text-transform:uppercase}
.hero-title .mark{background:var(--teal);padding:0 8px}
.hero-sub{margin-top:26px;font-size:18px;line-height:1.45;text-transform:uppercase;color:#d8dadb;width:440px}
.btn-outline{display:inline-block;margin-top:40px;border:2px solid var(--teal);padding:12px 22px;font-family:"Montserrat",Arial,sans-serif;font-size:12px;font-weight:700;letter-spacing:1px}

/* why */
.why{top:860px;height:560px;background:var(--paper)}
.video-frame{position:absolute;left:110px;top:120px;width:330px;height:250px;border:14px solid var(--teal);transform:translate(-20px,-20px)}
.video{position:absolute;left:110px;top:120px;width:330px;height:250px;background:linear-gradient(160deg,#3b3d3f,#1c1d1e)}
.video svg{position:absolute;left:140px;top:100px}
.why-copy{position:absolute;left:540px;top:105px;width:560px;color:var(--text-dark)}
.why-title{font-family:"Montserrat",Arial,sans-serif;font-weight:800;font-size:34px;text-transform:uppercase}
.teal-lead{font-family:"Montserrat",Arial,sans-serif;font-weight:700;font-size:15px;line-height:1.45;color:var(--teal);text-transform:uppercase;margin-top:14px}
.body-text{font-size:13px;line-height:1.7;margin-top:18px}
.btn-solid{display:inline-block;background:var(--teal);color:var(--white);padding:12px 24px;font-family:"Montserrat",Arial,sans-serif;font-size:12px;font-weight:700;letter-spacing:1px;margin-top:24px}
.stat{position:absolute;right:70px;top:440px;text-align:center;color:var(--text-dark)}
.stat-num{font-family:"Montserrat",Arial,sans-serif;font-weight:800;font-size:46px;color:var(--teal);line-height:1}
.stat-label{display:block;margin-top:6px;background:var(--white);border:1px solid #cfcfcf;padding:8px 14px;font-family:"Montserrat",Arial,sans-serif;font-size:12px;font-weight:700}

/* about */
.about{top:1420px;height:560px;background:var(--night)}
.about-photo{position:absolute;left:560px;top:0;width:640px;height:560px;background:radial-gradient(ellipse at 55% 45%,#3a3c3e 0%,#232526 55%,#1b1c1d 100%)}
.about-copy{position:absolute;left:110px;top:70px;width:520px}
.section-title{font-family:"Montserrat",Arial,sans-serif;font-weight:800;font-size:32px;text-transform:uppercase}
.about .body-text{color:#d7d9da}
.perks{position:absolute;left:110px;top:430px;display:flex;gap:46px}
.perk{text-align:center;font-family:"Montserrat",Arial,sans-serif;font-size:11px;font-weight:700;text-transform:uppercase;line-height:1.35}
.perk svg{display:block;margin:0 auto 10px}

/* testimonials */
.testimonials{top:1980px;height:520px;background:var(--teal)}
.testimonials::before{content:"";position:absolute;left:0;top:0;width:1200px;height:520px;background:linear-gradient(180deg,rgba(255,255,255,.08),rgba(0,0,0,.08))}
.testimonials .section-title{position:absolute;top:56px;width:1200px;text-align:center;font-size:28px}
.quote{position:absolute;top:150px;width:400px;background:var(--white);color:#555;padding:30px 34px;font-size:13px;line-height:1.7;text-align:center}
.quote::after{content:"";position:absolute;left:50%;bottom:-14px;margin-left:-14px;border:14px solid transparent;border-bottom:0;border-top-color:var(--white)}
.quote.side{opacity:.55;background:#d6f0ee}
.quote.side::after{border-top-color:#d6f0ee}
.quote.main{left:400px}
.quote.left{left:-240px}
.quote.right{left:1040px}
.client{position:absolute;top:340px;left:500px;width:200px;display:flex;align-items:center;gap:12px;color:var(--white)}
.avatar{width:52px;height:52px;border-radius:50%;background:linear-gradient(135deg,#6f7578,#3e4345);border:3px solid var(--white);flex:none}
.client-name{font-family:"Montserrat",Arial,sans-serif;font-weight:700;font-size:13px}
.client-role{font-size:11px}
.dots{position:absolute;top:440px;width:1200px;display:flex;justify-content:center;gap:10px}
.dots span{width:9px;height:9px;border-radius:50%;background:rgba(255,255,255,.5)}
.dots span.on{background:var(--white)}

/* brands */
.brands{top:2500px;height:190px;background:var(--white);color:var(--text-dark)}
.brands-title{position:absolute;left:80px;top:62px;font-family:"Montserrat",Arial,sans-serif;font-weight:800;font-size:20px;line-height:1.25;text-transform:uppercase}
.brand-list{position:absolute;left:400px;top:70px;display:flex;gap:110px;align-items:center}
.brand{font-family:"Open Sans",Arial,sans-serif;font-weight:600;font-size:24px;color:#5a5d60;display:flex;align-items:center;gap:10px}
.brand i{display:inline-block;width:16px;height:16px;background:#5a5d60}

/* contact */
.contact{top:2690px;height:420px;background:linear-gradient(180deg,#1f2a24,#141816)}
.contact-copy{position:absolute;top:50px;width:1200px;text-align:center}
.contact .section-title{font-size:24px}
.contact-sub{font-size:14px;text-transform:uppercase;letter-spacing:1px;color:#cfd3d1;margin-top:8px}
.form{position:absolute;left:200px;top:150px;width:800px}
.field{border-bottom:1px solid #6d7470;color:#b9bfbc;font-size:13px;padding:10px 0}
.row{display:flex;gap:40px;margin-bottom:24px}
.row .field{flex:1}
.form-foot{display:flex;justify-content:space-between;align-items:center;margin-top:28px}
.check{display:flex;align-items:center;gap:10px;font-size:12px;color:#cfd3d1}
.check span{width:16px;height:16px;background:var(--white)}
.submit{display:flex;align-items:center;gap:20px;font-size:11px;color:#cfd3d1}
.submit .btn-solid{margin:0}

/* footer */
.footer{top:3110px;height:270px;background:var(--ink)}
.footer .logo{left:80px;top:50px;font-size:26px}
.footer-cols{position:absolute;left:400px;top:50px;display:flex;gap:80px}
.footer-col h4{font-family:"Montserrat",Arial,sans-serif;font-size:13px;color:var(--teal);margin-bottom:14px}
.footer-col p{font-size:12px;color:var(--muted);line-height:1.9}
</style>
</head>
<body>

<section class="hero">
  <div class="hero-photo" role="img" aria-label="Close-up photograph of a gorilla in dark moody light"></div>
  <div class="logo"><span class="brand-name">TALLREED</span><small>MARKETING</small></div>
  <nav class="nav"><span>HOME</span><span>ABOUT</span><span>LOGOS</span><span>PORTFOLIO</span><span>CONTACT</span></nav>
  <div class="hero-copy">
    <h1 class="hero-title"><span class="mark">Socialia</span> and Seekly<br>Marketing Beasts</h1>
    <p class="hero-sub">Get performance-driven digital marketing leaders on your team</p>
    <span class="btn-outline">GET IN TOUCH</span>
  </div>
</section>

<section class="why">
  <div class="video-frame"></div>
  <div class="video" role="img" aria-label="Video still of the agency founder speaking">
    <svg width="50" height="50" viewBox="0 0 50 50"><circle cx="25" cy="25" r="24" fill="rgba(255,255,255,.85)"/><path d="M20 15 L35 25 L20 35 Z" fill="#242627"/></svg>
  </div>
  <div class="why-copy">
    <h2 class="why-title">Why Tallreed Marketing?</h2>
    <p class="teal-lead">Tallreed Marketing is the apex predator of the Socialia and Seekly marketing industries.</p>
    <p class="body-text">We are not the marketing agency that works on volume or keeps you waiting on reports. We drive real growth with focused campaigns, honest numbers and a team that treats your budget like its own. Our clients see more leads, lower costs and steady results month after month.</p>
    <span class="btn-solid">KNOW MORE</span>
  </div>
  <div class="stat"><div class="stat-num">220</div><span class="stat-label">DOGS SAVED THIS YEAR</span></div>
</section>

<section class="about">
  <div class="about-photo" role="img" aria-label="Faded photograph of a gorilla in shadow"></div>
  <div class="about-copy">
    <h2 class="section-title">About Us</h2>
    <p class="teal-lead">What sets us apart from other marketing agencies is our team of A-players.</p>
    <p class="body-text">Each team member has proven themselves to be in the top 1% of all marketers. They are the few practitioners who are passionate about what they do and have proven experience to back up their bold skills. Led by Marcus Vane, who has built and sold companies himself and written books from hard-won insight, the team at Tallreed Marketing specializes in your acquisition, lead generation and brand visibility.</p>
  </div>
  <div class="perks">
    <div class="perk">
      <svg width="40" height="40" viewBox="0 0 40 40" fill="none" stroke="#25b5ac" stroke-width="2.5"><path d="M4 32 L14 20 L22 26 L36 8"/><path d="M28 8 H36 V16"/></svg>
      More<br>Traffic
    </div>
    <div class="perk">
      <svg width="40" height="40" viewBox="0 0 40 40" fill="none" stroke="#25b5ac" stroke-width="2.5"><circle cx="20" cy="20" r="15"/><path d="M12 20 L18 26 L28 14"/></svg>
      Higher<br>Quality<br>Leads
    </div>
    <div class="perk">
      <svg width="40" height="40" viewBox="0 0 40 40" fill="none" stroke="#25b5ac" stroke-width="2.5"><rect x="6" y="22" width="6" height="12"/><rect x="17" y="14" width="6" height="20"/><rect x="28" y="6" width="6" height="28"/></svg>
      More<br>Sales
    </div>
  </div>
</section>

<section class="testimonials">
  <h2 class="section-title">Testimonials</h2>
  <div class="quote side left">Working with this team changed how we think about ads. Our leads doubled inside three months and the reporting was always clear and honest.</div>
  <div class="quote main">This crew simply delivered. They rebuilt our campaigns from the ground up, cut our cost per lead in half and kept us informed at every step. We finally have marketing that pays for itself.</div>
  <div class="quote side right">Fast, sharp and easy to work with. Our sales pipeline has never looked this healthy before.</div>
  <div class="client">
    <div class="avatar" role="img" aria-label="Client portrait"></div>
    <div><div class="client-name">Client Name</div><div class="client-role">Company Name</div></div>
  </div>
  <div class="dots"><span></span><span class="on"></span><span></span><span></span></div>
</section>

<section class="brands">
  <h3 class="brands-title">Name Brands<br>We've Worked With</h3>
  <div class="brand-list">
    <span class="brand"><i></i>Crestline</span>
    <span class="brand">Harbor Threads</span>
    <span class="brand">Sunvale</span>
  </div>
</section>

<section class="contact" role="img" aria-label="Dark jungle foliage background">
  <div class="contact-copy">
    <h2 class="section-title">Go in the jungle with true jungle kings</h2>
    <p class="contact-sub">Get into touch with us</p>
  </div>
  <div class="form">
    <div class="row"><div class="field">Your Full Name...</div><div class="field">Your Email Address...</div></div>
    <div class="field">Write a message for us...</div>
    <div class="form-foot">
      <div class="check"><span></span>Confirm you're human</div>
      <div class="submit"><span>We will answer<br>in 24 hours</span><span class="btn-solid">SEND NOW</span></div>
    </div>
  </div>
</section>

<footer class="footer">
  <div class="logo"><span class="brand-name">TALLREED</span><small>MARKETING</small></div>
  <div class="footer-cols">
    <div class="footer-col"><h4>Navigation</h4><p>About Us<br>Portfolio<br>Our Team<br>Contact</p></div>
    <div class="footer-col"><h4>Policy</h4><p>Terms of Use<br>Privacy<br>Cookies<br>Refunds</p></div>
    <div class="footer-col"><h4>Contacts</h4><p>Main Street 12<br>Riverside City<br>hello@tallreedmedia.com<br>www.tallreedmedia.com</p></div>
    <div class="footer-col"><h4>Social</h4><p>Socialia<br>Snapline<br>Worknet<br>Chirper</p></div>
  </div>
</footer>

</body>
</html>
```